Road Construction Company needs business cards

We would like a new business card designed for our business.

We're a road construction company based in Qld, Australia.

Can the business card please have the following information on it.

Name: Brent Malvoy
Position: General Manager
Phone: 0471 592 304
Email: Brent.malvoy@quendix.com.au
Address: 87 Harrowgate Ave, Pindarra, QLD, 4000
Website: www.quendix.com.au

Visually we'd like the card to be professional and simple.

Attached is our logo.

Our website is www.quendix.com.au

Target Market(s)

Men aged 25-60

Contact Information for Business Card

As listed in project description

Font styles to use
Serif

Requirements
Must have
• Large logo on back of card

```html
<!DOCTYPE html>
<html lang="en">
<head>
<meta charset="utf-8">
<title>Quendix Business Card</title>
<link href="https://fonts.googleapis.com/css2?family=Fira+Sans:wght@400;600;700&display=swap" rel="stylesheet">
<style>
  :root {
    --backdrop: #8f9295;
    --brand-blue: #0353a4;
    --accent-blue: #3a9fd8;
    --card-white: #ffffff;
    --ink: #1a1a1a;
  }
  * { margin: 0; padding: 0; box-sizing: border-box; }
  html, body {
    width: 1200px;
    height: 1200px;
    overflow: hidden;
    background: var(--backdrop);
    font-family: "Fira Sans", sans-serif;
  }
  .canvas { position: relative; width: 1200px; height: 1200px; }

  .card {
    position: absolute;
    width: 636px;
    height: 404px;
  }
  .card--front {
    left: 155px;
    top: 150px;
    background: var(--brand-blue);
    display: flex;
    align-items: center;
    justify-content: center;
  }
  .card--back {
    left: 373px;
    top: 673px;
    background: var(--card-white);
  }

  .wordmark {
    font-family: "Fira Sans", sans-serif;
    font-weight: 700;
    letter-spacing: 0.02em;
    line-height: 1;
  }
  .wordmark--front {
    color: var(--card-white);
    font-size: 66px;
    margin-top: -34px;
  }
  .wordmark--back {
    position: absolute;
    left: 61px;
    top: 185px;
    width: 188px;
    text-align: center;
    color: var(--brand-blue);
    font-size: 32px;
  }

  .divider {
    position: absolute;
    left: 268px;
    top: 123px;
    width: 2px;
    height: 160px;
    background: var(--brand-blue);
  }

  .person {
    position: absolute;
    left: 288px;
    top: 121px;
  }
  .person__name {
    color: var(--brand-blue);
    font-weight: 600;
    font-size: 20px;
    letter-spacing: 0.01em;
    text-transform: uppercase;
  }
  .person__role {
    color: var(--accent-blue);
    font-size: 16px;
    margin-top: 0px;
  }

  .contact-list {
    position: absolute;
    left: 294px;
    top: 180px;
    list-style: none;
  }
  .contact-list__item {
    display: flex;
    align-items: center;
    height: 28px;
    color: var(--ink);
    font-size: 15.5px;
  }
  .contact-list__icon {
    width: 16px;
    height: 16px;
    margin-right: 10px;
    fill: var(--brand-blue);
    flex-shrink: 0;
  }

  .accent-bar {
    position: absolute;
    left: 0;
    bottom: 0;
    width: 100%;
    height: 8px;
    display: flex;
  }
  .accent-bar__dark { flex: 1; background: var(--brand-blue); }
  .accent-bar__light { flex: 1; background: var(--accent-blue); }
</style>
</head>
<body>
<div class="canvas">

  <section class="card card--front" aria-label="Card front">
    <div class="wordmark wordmark--front">QUENDIX</div>
  </section>

  <section class="card card--back" aria-label="Card back">
    <div class="wordmark wordmark--back">QUENDIX</div>
    <div class="divider"></div>

    <div class="person">
      <div class="person__name">Brent Malvoy</div>
      <div class="person__role">General Manager</div>
    </div>

    <ul class="contact-list">
      <li class="contact-list__item">
        <svg class="contact-list__icon" viewBox="0 0 16 16" aria-hidden="true">
          <path d="M1 5.5C1 3.5 4 2.5 8 2.5s7 1 7 3v1.2h-3.5V5.2c-1-.4-2.2-.5-3.5-.5s-2.5.1-3.5.5v1.5H1z"/>
          <path d="M3.5 8.2 5 6.5h6l1.5 1.7V13h-9z"/>
        </svg>
        0471 592 304
      </li>
      <li class="contact-list__item">
        <svg class="contact-list__icon" viewBox="0 0 16 16" aria-hidden="true">
          <path d="M1 3.5h14v9H1z" fill="none" stroke="#0353a4" stroke-width="1.4"/>
          <path d="M1 3.5 8 9l7-5.5" fill="none" stroke="#0353a4" stroke-width="1.4"/>
        </svg>
        Brent.malvoy@quendix.com.au
      </li>
      <li class="contact-list__item">
        <svg class="contact-list__icon" viewBox="0 0 16 16" aria-hidden="true">
          <circle cx="8" cy="8" r="6.5" fill="none" stroke="#0353a4" stroke-width="1.4"/>
          <ellipse cx="8" cy="8" rx="2.8" ry="6.5" fill="none" stroke="#0353a4" stroke-width="1.2"/>
          <path d="M1.5 8h13M2.5 5h11M2.5 11h11" stroke="#0353a4" stroke-width="1.1"/>
        </svg>
        www.quendix.com.au
      </li>
      <li class="contact-list__item">
        <svg class="contact-list__icon" viewBox="0 0 16 16" aria-hidden="true">
          <path d="M8 1a5 5 0 0 0-5 5c0 3.6 5 9 5 9s5-5.4 5-9a5 5 0 0 0-5-5zm0 7a2 2 0 1 1 0-4 2 2 0 0 1 0 4z"/>
        </svg>
        87 Harrowgate Ave, Pindarra, QLD, 4000
      </li>
    </ul>

    <div class="accent-bar">
      <div class="accent-bar__dark"></div>
      <div class="accent-bar__light"></div>
    </div>
  </section>

</div>
</body>
</html>
```